New boutique IT consultancy needs business card

I need a business card and logo for my IT consultancy business, called 'Quenmarlo' . I want it to make me look bigger than I am. I want it to look classy, and modern. Simple design, that will be easy for me to translate into my webpage etc. The business card should be bold, and different.

The logo should emphasise the 'y' as used in quenmarlo

Target Market(s)

IT divisions in other companies

Industry/Entity Type

Business

Contact Information for Business Card

Doreen Pakfield
Director
+61 437 918 205
dpakfield@quenmarlo-mail.test

```html
<!DOCTYPE html>
<html lang="en">
<head>
<meta charset="utf-8">
<title>Quenmarlo – Business Card</title>
<link href="https://fonts.googleapis.com/css2?family=Lato:wght@400;700;900&display=swap" rel="stylesheet">
<style>
  :root {
    --bg: #3a3a3c;
    --card: #fbfbfb;
    --ink: #1c1c1c;
    --magenta: #d0157f;
    --blue: #3c55b0;
    --shadow: rgba(0, 0, 0, 0.45);
  }
  * { box-sizing: border-box; margin: 0; padding: 0; }
  html, body {
    width: 1200px;
    height: 997px;
    overflow: hidden;
    background: var(--bg);
    font-family: "Lato", Arial, sans-serif;
    color: var(--ink);
  }
  .stage {
    position: relative;
    width: 1200px;
    height: 997px;
  }
  .card {
    position: absolute;
    left: 250px;
    width: 700px;
    height: 400px;
    background: var(--card);
    border-radius: 22px;
    box-shadow: 0 14px 30px var(--shadow);
  }
  .card--front { top: 60px; }
  .card--back { top: 537px; }

  .wordmark {
    display: flex;
    align-items: center;
    gap: 12px;
    font-weight: 900;
    color: var(--ink);
    letter-spacing: 0.5px;
  }
  .wordmark__square {
    display: block;
    background: var(--magenta);
  }
  .card--front .wordmark {
    position: absolute;
    left: 50%;
    top: 50%;
    transform: translate(-50%, -50%);
    font-size: 56px;
  }
  .card--front .wordmark__square { width: 30px; height: 30px; }

  .card--back .wordmark {
    position: absolute;
    right: 44px;
    top: 70px;
    font-size: 32px;
  }
  .card--back .wordmark__square { width: 18px; height: 18px; }

  .divider {
    position: absolute;
    left: 44px;
    right: 44px;
    top: 196px;
    height: 2px;
    background: var(--magenta);
  }
  .person {
    position: absolute;
    left: 44px;
    top: 140px;
  }
  .person__name {
    font-size: 20px;
    color: var(--magenta);
    font-weight: 400;
  }
  .person__role {
    font-size: 19px;
    margin-top: 2px;
  }
  .contacts {
    position: absolute;
    left: 44px;
    top: 226px;
    list-style: none;
    font-size: 17px;
  }
  .contacts li {
    display: flex;
    align-items: center;
    gap: 12px;
    height: 40px;
  }
  .contacts svg { width: 18px; height: 18px; fill: var(--magenta); flex: none; }

  .company {
    position: absolute;
    right: 44px;
    top: 220px;
    text-align: right;
    font-size: 16px;
    line-height: 1.4;
  }
  .company__name {
    color: var(--magenta);
    font-weight: 700;
    font-size: 18px;
  }
</style>
</head>
<body>
<main class="stage">

  <section class="card card--front" aria-label="Card front">
    <div class="wordmark">
      <span class="wordmark__square"></span>
      <span class="wordmark__name">Quenmarlo</span>
    </div>
  </section>

  <section class="card card--back" aria-label="Card back">
    <div class="wordmark">
      <span class="wordmark__square"></span>
      <span class="wordmark__name">Quenmarlo</span>
    </div>

    <div class="person">
      <p class="person__name">Doreen Pakfield</p>
      <p class="person__role">Director</p>
    </div>

    <div class="divider"></div>

    <ul class="contacts">
      <li>
        <svg viewBox="0 0 24 24" aria-hidden="true"><path d="M6.6 10.8a15.1 15.1 0 0 0 6.6 6.6l2.2-2.2a1 1 0 0 1 1-.25 11.4 11.4 0 0 0 3.6.57 1 1 0 0 1 1 1V20a1 1 0 0 1-1 1A17 17 0 0 1 3 4a1 1 0 0 1 1-1h3.5a1 1 0 0 1 1 1c0 1.25.2 2.45.57 3.57a1 1 0 0 1-.25 1z"/></svg>
        <span>+61 437 918 205</span>
      </li>
      <li>
        <svg viewBox="0 0 24 24" aria-hidden="true"><path d="M2 5h20v14H2z M4 7v.5l8 5 8-5V7l-8 5z" fill-rule="evenodd"/></svg>
        <span>dpakfield@quenmarlo-mail.test</span>
      </li>
      <li>
        <svg viewBox="0 0 24 24" aria-hidden="true"><path d="M12 2a10 10 0 1 0 0 20 10 10 0 0 0 0-20zm6.9 9h-3a15 15 0 0 0-1.3-5.6A8 8 0 0 1 18.9 11zM12 4.1c.9 1.2 1.8 3.6 1.9 6.9h-3.8c.1-3.3 1-5.7 1.9-6.9zM9.4 5.4A15 15 0 0 0 8.1 11h-3a8 8 0 0 1 4.3-5.6zM5.1 13h3a15 15 0 0 0 1.3 5.6A8 8 0 0 1 5.1 13zm6.9 6.9c-.9-1.2-1.8-3.6-1.9-6.9h3.8c-.1 3.3-1 5.7-1.9 6.9zm2.6-1.3a15 15 0 0 0 1.3-5.6h3a8 8 0 0 1-4.3 5.6z"/></svg>
        <span>www.quenmarlo.com</span>
      </li>
    </ul>

    <address class="company" style="font-style: normal;">
      <p class="company__name">Quenmarlo Pvt Ltd.</p>
      <p>48 Larkspur lane, Orbit suite</p>
      <p>Pune, India.</p>
    </address>
  </section>

</main>
</body>
</html>
```